Italian restaurant needs a flyer to promote wine tasting and wine pairing tours

Need a designer to create one flyer for print and digital use.

(3 pages all either postcard or 1/3 page)Intro page, wine tasting and wine pairing page, wine pairing and cruise page

We are Www.lunaverdetrattoria.com an top rated Italian restaurant in CABO San Lucas mexico. Our info and history is on the website. We are a fun, cozy bistro ambience that makes you feel like you are in Italy.

Get to know the great tastes of Rome right here in CABO San Lucas at Corvale Bistro. Farm and sea to table and select national and international wines . We begin with a brief introduction of the restaurant including a quick Salute to the kitchen then sit at our reserved table for a fun and tasty wine food pairing.

Our Founding Chef and In House Sommelier join forces to create four fabulous farm and sea to table dishes, using the freshest ingredients from local sources and only the top wines from small vineyards. Guests are guided through four wine & food pairings, with a some fun facts about wine and the wine producing regions of Mexico. A lively resort casual setting and a night you will never forget.

Wine & Dine Pairing Session includes:
* Welcome cocktail!
* 4-Course Wine Pairing menu
* Each course paired with local wines
* After Tasting Night cap
* Regional history, Wine tasting tips, trivia, and prizes!
* Guests receive 20% off their next reservation
* Everyday at 5:30pm and 9:30pm for one hour and 45 minutes.
* Limited to 10 guests per session please reserve in advance.
* 69usd X person. Tax included .

Target Market(s)

Wine lovers coming to CABO San Lucas

Industry/Entity Type

Restaurant

Font styles to use
Serif

Requirements
Must have
• More image and less text with an elegant yet fun setting
• Must have wine and dine description:
• Get to know the great tastes of Rome right here in CABO San Lucas at Corvale Bistro. Farm and sea to table and select national and international wines . We begin with a brief introduction of the restaurant including a quick Salute to the kitchen then sit at our reserved table for a fun and tasty wine food pairing.
• Our Founding Chef and In House Sommelier join forces to create four fabulous farm and sea to table dishes, using the freshest ingredients from local sources and only the top wines from small vineyards. Guests are guided through four wine & food pairings, with a some fun facts about wine and the wine producing regions of Mexico. A lively resort casual setting and a night you will never forget.
• Wine & Dine Pairing Session includes:
• * Welcome cocktail!
• * 4-Course Wine Pairing menu
• * Each course paired with local wines
• * After Tasting Night cap
• * Regional history, Wine tasting tips, trivia, and prizes!
• * Guests receive 20% off their next reservation
• * Everyday at 5:30pm and 9:30pm for one hour and 45 minutes.
• * Limited to 10 guests per session please reserve in advance.
• * 69usd X person. Tax included .
• amd must have wine tasting description:
• One hour of fun and flavor!
• Join our in house sommelier in this small group, one hour , lively happy hour party that includes ample tastes of 3 fine wines paired with authentic Italian gourmet appetizers and seasonal menu favorites. Let us share the best of Bajas wines amd perfectly paired tasting menu before hitting the town.
• This Wine Tasting Happy hour includes:
• * Welcome cocktail!
• * 4-Course Tasting menu
• * Each course paired with Baja local wines
• * Starts at 5pm or 6pm. Arrive 5 minutes prior for check in. Space is limited to 20 guests so advanced reservations are recommended.
• * 25usd per person tax included.
• Colors should be like our website www.lunaverdetrattoria.com
• Files must be editable
Nice to have
• Want this to focus on promoting the restaurant and tours
Should not have
• Errors

```html
<!DOCTYPE html>
<html lang="en">
<head>
<meta charset="utf-8">
<title>Corvale Bistro – Wine Pairing &amp; Tasting Postcards</title>
<link href="https://fonts.googleapis.com/css2?family=Alfa+Slab+One&family=Anton&family=Cinzel:wght@600&family=PT+Sans:wght@400&display=swap" rel="stylesheet">
<style>
  :root{
    --page:#2a1b14;
    --card-light:#7a2516;
    --card-mid:#5e1810;
    --card-dark:#3a0a07;
    --orange:#f0a024;
    --gold:#e8bf3a;
    --white:#ffffff;
    --text:#f6ece6;
    --photo-a:#2b0c08;
    --photo-b:#6a2a14;
  }
  *{box-sizing:border-box;margin:0;padding:0}
  html,body{width:1200px;height:1200px;overflow:hidden;background:var(--page)}
  body{position:relative;font-family:"PT Sans",sans-serif;color:var(--text)}

  .postcard{
    position:absolute;left:63px;width:1058px;height:514px;overflow:hidden;
    background:radial-gradient(ellipse at 35% 40%, var(--card-light) 0%, var(--card-mid) 55%, var(--card-dark) 100%);
    box-shadow:0 10px 24px rgba(0,0,0,.55);
  }
  .postcard--intro{top:75px}
  .postcard--tasting{top:634px}

  .photo{position:absolute;top:0;bottom:0;right:0}
  .postcard--intro .photo{
    left:560px;
    background:linear-gradient(90deg, rgba(43,12,8,0) 0%, var(--photo-a) 25%, var(--photo-b) 60%, var(--photo-a) 100%);
  }
  .postcard--tasting .photo{
    left:790px;top:70px;
    background:linear-gradient(90deg, rgba(43,12,8,0) 0%, var(--photo-a) 28%, var(--photo-b) 65%, var(--photo-a) 100%);
  }

  .brand{position:absolute;display:flex;align-items:center;gap:8px}
  .brand__dot{border-radius:50%;background:var(--gold);flex:none}
  .brand__name{font-family:"Cinzel",serif;font-weight:600;color:var(--gold);white-space:nowrap}
  .postcard--intro .brand{left:40px;top:82px}
  .postcard--intro .brand__dot{width:14px;height:14px}
  .postcard--intro .brand__name{font-size:21px}
  .postcard--tasting .brand{left:90px;top:36px}
  .postcard--tasting .brand__dot{width:9px;height:9px}
  .postcard--tasting .brand__name{font-size:14px}

  .headline{position:absolute;left:288px;top:46px;line-height:1;font-weight:400}
  .headline__top{font-family:"PT Sans",sans-serif;font-size:54px;color:var(--white)}
  .headline__main{font-family:"Anton",sans-serif;font-size:72px;color:var(--orange);letter-spacing:6px;margin-top:2px}

  .intro-copy{position:absolute;left:31px;top:228px;width:430px;font-size:15px;line-height:18.9px}
  .intro-copy p + p{margin-top:18.9px;text-align:justify}

  .section-title{font-size:19px;color:var(--orange);font-weight:400;display:inline-block;border-bottom:1.5px solid var(--text);padding-bottom:3px;line-height:1.2}

  .feature-list{list-style:none}
  .feature-list li{position:relative;padding-left:30px;font-size:15px;line-height:18.8px}
  .feature-list li::before{content:"";position:absolute;left:4px;top:6px;width:8px;height:8px;border-radius:50%;background:var(--orange)}

  .session{position:absolute;left:35px;top:104px;width:310px}
  .session .feature-list{margin-top:19px}
  .session .feature-list li{margin-bottom:12px}

  .tasting{position:absolute;left:376px;top:40px;width:448px}
  .tasting__headline{font-family:"Alfa Slab One",serif;font-size:30px;font-weight:400;color:var(--orange);white-space:nowrap;line-height:1.1}
  .tasting__copy{margin-top:26px;font-size:15px;line-height:18.8px}
  .tasting .section-title{margin-top:14px}
  .tasting .feature-list{margin-top:14px;width:350px}
  .tasting .feature-list li{margin-bottom:9px}
</style>
</head>
<body>

<section class="postcard postcard--intro">
  <div class="photo" role="img" aria-label="Photo of a wine decanter, glasses and a row of red wine bottles with corks"></div>
  <div class="brand"><span class="brand__dot"></span><span class="brand__name">Corvale Bistro</span></div>
  <h1 class="headline">
    <div class="headline__top">WELCOME</div>
    <div class="headline__main">COCKTAIL!</div>
  </h1>
  <div class="intro-copy">
    <p>Get to know the great tastes of Rome right here in CABO San Lucas at Corvale Bistro. Farm and sea to table and select national and international wines . We begin with a brief introduction of the restaurant including a quick Salute to the kitchen then sit at our reserved table for a fun and tasty wine food pairing.</p>
    <p>Our Founding Chef and In House Sommelier join forces to create four fabulous farm and sea to table dishes, using the freshest ingredients from local sources and only the top wines from small vineyards. Guests are guided through four wine &amp; food pairings, with a some fun facts about wine and the wine producing regions of Mexico. A lively resort casual setting and a night you will never forget.</p>
  </div>
</section>

<section class="postcard postcard--tasting">
  <div class="photo" role="img" aria-label="Photo of a wine decanter, glass and red wine bottles"></div>
  <div class="brand"><span class="brand__dot"></span><span class="brand__name">Corvale Bistro</span></div>

  <div class="session">
    <h2 class="section-title">Wine &amp; Dine Pairing Session</h2>
    <ul class="feature-list">
      <li>Welcome cocktail!</li>
      <li>4-Course Wine Pairing menu</li>
      <li>Each course paired with local wines</li>
      <li>After Tasting Night cap</li>
      <li>Regional history, Wine tasting tips, trivia, and prizes!</li>
      <li>Guests receive 20% off their next reservation</li>
      <li>Everyday at 5:30pm and 9:30pm for one hour and 45 minutes.</li>
      <li>Limited to 10 guests per session please reserve in advance.</li>
      <li>69usd X person. Tax included</li>
    </ul>
  </div>

  <div class="tasting">
    <h2 class="tasting__headline">One hour of fun &amp; flavor!</h2>
    <p class="tasting__copy">Join our in house sommelier in this small group, one hour , lively happy hour party that includes ample tastes of 3 fine wines paired with authentic Italian gourmet appetizers and seasonal menu favorites. Let us share the best of Bajas wines and perfectly paired tasting menu before hitting the town.</p>
    <h3 class="section-title">This Wine Tasting Happy hour</h3>
    <ul class="feature-list">
      <li>Welcome cocktail!</li>
      <li>4-Course Tasting menu</li>
      <li>Each course paired with Baja local wines</li>
      <li>Regional history, Wine tasting tips, trivia, and prizes!</li>
      <li>Guests receive 20% off their next reservation</li>
      <li>Starts at 5pm or 6pm. Arrive 5 minutes prior for check in. Space is limited to 20 guests so advanced reservations are recommended.</li>
      <li>25usd per person tax included.</li>
    </ul>
  </div>
</section>

</body>
</html>
```